Clever & creative business card needed for a pediatric dentist.

We need a business card for a pediatric dentist that is building a brand-new pediatric dental practice. He is funny, outgoing, and sociable, and he hopes to give his business card to dentists and pediatricians so that he can give them information of where to refer infants, children, and teenagers that need high quality and attainable dental care.

The name of the dental practice is Copper Fern Pediatric Dentistry. Logo design .png / .pdf/ .jpg are provided to aid in the design.

The dentist's last name is Tolvan (which sounds like "burger", as in "hamburger” or “cheeseburger"). Since it is pediatric practice, kudos will be given to designs that implement a little joke into the design - but hopefully in a small or hidden way (such as putting something like a cheeseburger on the back of the card, or hiding it an an abstract way).

Thank you!

Please make a design that incorporates colors. It should be fun! Not too serious. It does not have to follow the color scheme of the logos.

```html
<!DOCTYPE html>
<html lang="en">
<head>
<meta charset="utf-8">
<title>Copper Fern Pediatric Dentistry — Business Card</title>
<link href="https://fonts.googleapis.com/css2?family=Montserrat:wght@700&family=Nunito+Sans:wght@400;600;700&display=swap" rel="stylesheet">
<style>
  :root{
    --bg:#e9eaea;
    --card:#f7f7f6;
    --ink:#2f3331;
    --ink-soft:#4a4f4c;
    --green-dark:#2f9a4a;
    --green:#55b164;
    --green-mid:#7cc283;
    --green-light:#a9d6a8;
    --green-pale:#cfe6cc;
    --divider:#3b3f3d;
  }
  *{box-sizing:border-box;margin:0;padding:0}
  html,body{width:1200px;height:794px;overflow:hidden}
  body{background:var(--bg);font-family:"Nunito Sans",sans-serif;color:var(--ink);position:relative}

  .card{position:absolute;width:560px;height:320px;background:var(--card);
        box-shadow:0 2px 6px rgba(0,0,0,.12);overflow:hidden}
  .card--front{left:30px;top:237px}
  .card--back{left:610px;top:237px}

  /* Front */
  .brand{position:absolute;left:34px;top:122px;width:200px;text-align:center}
  .brand__mark{display:block;width:34px;height:34px;border-radius:50%;background:var(--green-mid);margin:0 auto 12px}
  .brand__name{font-weight:700;font-size:21px;line-height:1.15;color:var(--ink)}
  .divider{position:absolute;left:248px;top:70px;width:2px;height:170px;background:var(--divider)}

  .contact{position:absolute;left:276px;top:62px;width:270px}
  .contact__joke{display:block;width:70px;height:34px;margin:0 0 6px 58px}
  .contact__name{font-family:"Montserrat",sans-serif;font-weight:700;font-size:18px;color:var(--green-dark);letter-spacing:.2px}
  .contact__title{font-size:13px;color:var(--ink-soft);margin:2px 0 12px}
  .contact__list{list-style:none}
  .contact__item{display:flex;align-items:flex-start;gap:10px;font-size:13px;line-height:1.5;color:var(--ink-soft)}
  .contact__item svg{flex:0 0 14px;width:14px;height:14px;margin-top:3px;stroke:var(--green);fill:none;stroke-width:1.6;stroke-linecap:round;stroke-linejoin:round}

  .band{position:absolute;left:0;right:0;bottom:0;height:12px;display:flex}
  .band span{flex:1}
  .band span:nth-child(1){background:var(--green-dark)}
  .band span:nth-child(2){background:var(--green)}
  .band span:nth-child(3){background:var(--green-mid)}
  .band span:nth-child(4){background:var(--green-light)}
  .band span:nth-child(5){background:var(--green-pale)}

  /* Back */
  .back__decor{position:absolute;right:0;top:0;width:290px;height:320px;
     background:radial-gradient(ellipse at 75% 25%, var(--green-pale) 0%, rgba(207,230,204,.55) 45%, rgba(247,247,246,0) 80%);
     border-bottom-left-radius:140px}
  .back__brand{position:absolute;left:30px;top:44px;display:flex;align-items:center;gap:8px}
  .back__brand .brand__mark{width:22px;height:22px;margin:0}
  .back__brand .brand__name{font-size:13px}
  .back__greeting{position:absolute;left:30px;top:90px;width:300px;font-size:17px;line-height:1.35;color:var(--ink)}
  .back__note{position:absolute;left:30px;bottom:34px;font-size:13px;color:var(--ink-soft);display:flex;align-items:center;gap:8px}
  .back__note::before{content:"";width:6px;height:6px;border-radius:50%;background:var(--green)}
</style>
</head>
<body>

<section class="card card--front">
  <div class="brand">
    <span class="brand__mark"></span>
    <p class="brand__name">Copper Fern<br>Pediatric Dentistry</p>
  </div>
  <div class="divider"></div>
  <div class="contact">
    <svg class="contact__joke" viewBox="0 0 70 34" role="img" aria-label="Small burger bun illustration hinting at the dentist's name">
      <path d="M4 32 A31 28 0 0 1 66 32 Z" fill="var(--green-pale)"/>
    </svg>
    <h1 class="contact__name">ELIAS TOLVAN, D.M.D.</h1>
    <p class="contact__title">Board-Certified Pediatric Dentist</p>
    <ul class="contact__list">
      <li class="contact__item"><svg viewBox="0 0 16 16"><path d="M3 2h3l1 3-2 1a8 8 0 0 0 5 5l1-2 3 1v3a1 1 0 0 1-1 1A12 12 0 0 1 2 3a1 1 0 0 1 1-1z"/></svg>(555) 014-2200</li>
      <li class="contact__item"><svg viewBox="0 0 16 16"><rect x="2" y="6" width="12" height="6" rx="1"/><path d="M4 6V2h8v4M4 10h8v4H4z"/></svg>(555) 014-2210</li>
      <li class="contact__item"><svg viewBox="0 0 16 16"><rect x="1.5" y="3.5" width="13" height="9" rx="1"/><path d="M2 4l6 5 6-5"/></svg>hello@copperfernkids.com</li>
      <li class="contact__item"><svg viewBox="0 0 16 16"><circle cx="8" cy="8" r="6.5"/><path d="M1.5 8h13M8 1.5c2 2 2 11 0 13M8 1.5c-2 2-2 11 0 13"/></svg>copperfernkids.com</li>
      <li class="contact__item"><svg viewBox="0 0 16 16"><path d="M8 15s5-5 5-9A5 5 0 0 0 3 6c0 4 5 9 5 9z"/><circle cx="8" cy="6" r="1.8"/></svg>48 Meadowbrook Lane, Suite 210<br>Halden, CT 06490</li>
    </ul>
  </div>
  <div class="band"><span></span><span></span><span></span><span></span><span></span></div>
</section>

<section class="card card--back">
  <div class="back__decor" role="img" aria-label="Large faint brand decoration in soft green"></div>
  <div class="back__brand">
    <span class="brand__mark"></span>
    <p class="brand__name">Copper Fern</p>
  </div>
  <p class="back__greeting">We look forward to seeing you at your next appointment</p>
  <p class="back__note">If unable to keep this appointment, kindly give us 48 hours notice</p>
</section>

</body>
</html>
```